Wine Label Design for the red wine named “Amber Over Stone” or “A/S”

Create an elegant yet simple (less is more) label for a red, full-bodied wine from a family-owned Herzegovinian vineyard by the river with 9 names. You can use elements such as the Calopteryx virgo, possibly the river shape, and ensure a coherent storytelling of the unique vineyard’s locality and meticulous, hand-picked grape cultivation.
Let’s craft a label that is not just seen, but is experienced and remembered.

Target Market(s)

Wine lovers that appreciate high quality wines

Industry/Entity Type

Wine, Family owned small producer

Requirements
Must have
• Name A/S, front and back label. Premium feel, uniqueness. Simple but interesting.
Nice to have
• Please see the images below as an idea of various directions. I am also leaning to embossed image on the label
Should not have
• Should not be overcrowded with text, too many images and objects

```html
<!DOCTYPE html>
<html lang="en">
<head>
<meta charset="utf-8">
<title>Amber Over Stone – Front Label</title>
<link rel="stylesheet" href="https://fonts.googleapis.com/css2?family=Bodoni+Moda:opsz,wght@6..96,400&family=Montserrat:wght@500&display=swap">
<style>
  :root {
    --backdrop: #e8ded1;
    --label: #2a2626;
    --crimson: #9c3047;
  }
  html, body {
    margin: 0;
    padding: 0;
    width: 1200px;
    height: 1200px;
    overflow: hidden;
    background: var(--backdrop);
  }
  .canvas {
    position: relative;
    width: 1200px;
    height: 1200px;
  }
  .front-label {
    position: absolute;
    left: 218px;
    top: 100px;
    width: 763px;
    height: 1000px;
    background: var(--label);
    box-shadow: 0 10px 40px rgba(60, 40, 30, 0.18);
  }
  .brand-mark {
    position: absolute;
    left: 138px;
    top: 300px;
    width: 72px;
    height: 72px;
    border-radius: 50%;
    background: var(--crimson);
  }
  .wine-name {
    position: absolute;
    left: 125px;
    top: 505px;
    margin: 0;
    font-family: "Bodoni Moda", "Didot", serif;
    font-weight: 400;
    font-size: 86px;
    line-height: 82px;
    letter-spacing: -0.02em;
    color: var(--crimson);
  }
  .wine-name span { display: block; }
  .label-foot {
    position: absolute;
    left: 125px;
    right: 107px;
    top: 876px;
    display: flex;
    justify-content: space-between;
    font-family: "Montserrat", "Helvetica", sans-serif;
    font-weight: 500;
    font-size: 15px;
    letter-spacing: 0.22em;
    text-transform: uppercase;
    color: var(--crimson);
  }
</style>
</head>
<body>
  <main class="canvas">
    <section class="front-label" aria-label="Front wine label">
      <div class="brand-mark" aria-hidden="true"></div>
      <h1 class="wine-name">
        <span>Amber</span>
        <span>Over</span>
        <span>Stone</span>
      </h1>
      <div class="label-foot">
        <span class="label-foot__type">Hand Crafted Wine</span>
        <span class="label-foot__volume">750 ml</span>
      </div>
    </section>
  </main>
</body>
</html>
```